TKR Engineering Pty Ltd

I have already had nox welding and fabrication cards made , my business has changed too TKR engineering Pty Ltd so I need my logo changed on the cards
one side have my logo then the other side have what we do.
front side logo and details
owner /operator : Curtis Halvorsen
email: tkr.works@examplemail.net
number: 0491537204
ABN: 52 604 381 927
ACN: 728 391 056
on back have in dot points what we do:
* structural steel erection
* precast panels
* site welding
*steel alteration & repair
* rigging & dogging
*labour hire
Contact Information for Business Card
all details in breif
Look and feel
Each slider illustrates characteristics of the customer's brand and the style your logo design should communicate.

```html
<!DOCTYPE html>
<html lang="en">
<head>
<meta charset="utf-8">
<title>TKR Engineering Pty Ltd – Business Card</title>
<link rel="stylesheet" href="https://fonts.googleapis.com/css2?family=Arimo:wght@400;700&display=swap">
<style>
  :root {
    --backdrop: #142233;
    --card: #ffffff;
    --rust: #96513f;
    --navy: #1c2b3b;
    --ink-light: #ffffff;
  }
  * { margin: 0; padding: 0; box-sizing: border-box; }
  html, body {
    width: 1200px;
    height: 1000px;
    overflow: hidden;
    background: var(--backdrop);
    font-family: "Arimo", Arial, sans-serif;
  }
  .stage {
    position: relative;
    width: 1200px;
    height: 1000px;
  }
  .card {
    position: absolute;
    width: 540px;
    height: 310px;
    background: var(--card);
    overflow: hidden;
  }
  .card-front { left: 110px; top: 150px; display: flex; }
  .card-back  { left: 550px; top: 540px; }

  .front-brand {
    width: 46%;
    display: flex;
    align-items: center;
    justify-content: center;
  }
  .brand-lockup {
    display: flex;
    align-items: center;
    gap: 10px;
  }
  .brand-mark {
    width: 18px;
    height: 18px;
    background: var(--navy);
  }
  .brand-name {
    color: var(--navy);
    font-weight: 700;
    font-size: 17px;
    line-height: 1.2;
    letter-spacing: 0.02em;
  }
  .front-details {
    width: 54%;
    background: var(--rust);
    color: var(--ink-light);
    display: flex;
    flex-direction: column;
    justify-content: center;
    padding-left: 44px;
    font-size: 17px;
    line-height: 1.18;
  }
  .owner-name {
    font-weight: 700;
    font-size: 18px;
    margin-bottom: 2px;
  }

  .services {
    position: absolute;
    left: 150px;
    top: 92px;
    list-style: none;
    border-left: 3px solid var(--rust);
    padding: 6px 0 6px 20px;
    color: var(--navy);
    font-size: 20px;
    line-height: 1.1;
  }
</style>
</head>
<body>
<main class="stage">
  <section class="card card-front" aria-label="Business card front">
    <div class="front-brand">
      <div class="brand-lockup">
        <span class="brand-mark" aria-hidden="true"></span>
        <span class="brand-name">TKR<br>ENGINEERING<br>PTY LTD</span>
      </div>
    </div>
    <div class="front-details">
      <p class="owner-name">Curtis Halvorsen</p>
      <p>tkr.works@examplemail.net</p>
      <p>0491537204</p>
      <p>ABN: 52 604 381 927</p>
      <p>ACN: 728 391 056</p>
    </div>
  </section>

  <section class="card card-back" aria-label="Business card back">
    <ul class="services">
      <li>structural steel erection</li>
      <li>precast panels</li>
      <li>site welding</li>
      <li>steel alteration &amp; repair</li>
      <li>rigging &amp; dogging</li>
      <li>labour hire</li>
    </ul>
  </section>
</main>
</body>
</html>
```